The Tidegrove Newsletter For My Monthly Investment Newsletters

I'm looking to create two beautiful newsletter template for my new financial planning and investment firm. I keep my newsletters short and sweet as I feel less is more. One newsletter is for investment updates - I send that to clients and prospects. The other is more of an update for clients only.

I'm going to be using Mailchimp & Constant Contact so please make sure I can use that template there.

My newsletter typically goes out monthly. There are two versions - one for clients and one for prospects. Sometimes, information is applicable for clients only.

The newsletter brief should have the month and year in it like
The Tidegrove Newsletter: March 2020.

The other can be

The Tidegrove Update: March 2020 (for more administrative announcements).

Target Market(s)

Investors

Industry/Entity Type

Investment Advisory

Font styles to use
Sans Serif

Colors

Designer to choose colors to be used in the design.

Requirements
Must have
• Clean
• professional
• Modern feel
• Less is more.
• Colors should match and be in sync my logo.
• I'm going to be using Mailchimp & Constant Contact so please make sure I can use that template there.
Nice to have
• Please follow the must haves

```html
<!DOCTYPE html>
<html lang="en">
<head>
<meta charset="utf-8">
<title>Tidegrove Newsletter Templates</title>
<link rel="stylesheet" href="https://fonts.googleapis.com/css2?family=Libre+Baskerville:wght@700&family=Roboto:wght@300;400;500;700&display=swap">
<style>
:root{
  --page:#d5d5d5;
  --navy:#123a5e;
  --ink:#121c28;
  --orange:#e07a1b;
  --orange-hi:#f0ab12;
  --orange-lo:#ec650f;
  --teal:#21b2bd;
  --teal-deep:#0e3a4a;
  --night:#11222c;
  --text:#3a4250;
  --grey-text:#555b63;
  --white:#ffffff;
}
*{box-sizing:border-box;margin:0;padding:0}
html,body{width:1023px;height:1200px;overflow:hidden}
body{background:var(--page);font-family:"Roboto",Arial,sans-serif;position:relative}
.serif{font-family:"Libre Baskerville",Georgia,serif}

.template{position:absolute;top:33px;width:457px;overflow:hidden;background:var(--white)}
.template--update{left:46px;height:1133px}
.template--newsletter{left:528px;height:1060px}

.abs{position:absolute}
.brand{position:absolute;left:0;width:100%;display:flex;justify-content:center;align-items:center;gap:10px}
.brand__dot{width:26px;height:26px;border-radius:50%}
.brand__name{font-family:"Libre Baskerville",Georgia,serif;font-weight:700;font-size:34px;letter-spacing:.5px}

.headline{position:absolute;left:0;width:100%;text-align:center;font-family:"Libre Baskerville",Georgia,serif;font-weight:700;font-size:33px;line-height:36px;letter-spacing:.5px}
.date-pill{position:absolute;border-radius:24px;color:var(--white);font-family:"Libre Baskerville",Georgia,serif;font-weight:700;font-size:16px;display:flex;align-items:center;justify-content:center;letter-spacing:.5px}

/* update template */
.hero-snow{top:0;left:0;width:457px;height:420px;background:linear-gradient(180deg,#c9d8e8 0%,#dfe8f2 35%,#eef3f8 65%,#ffffff 100%)}
.feature-row{position:absolute;left:0;width:457px;height:80px}
.feature-row__badge{position:absolute;left:45px;top:0;width:78px;height:78px;border-radius:50%;display:flex;align-items:center;justify-content:center}
.feature-row__title{position:absolute;left:135px;top:0;font-weight:700;font-size:14px;color:var(--ink)}
.feature-row__body{position:absolute;left:136px;top:22px;width:300px;font-size:10.8px;line-height:15px;color:var(--text)}

.split{position:absolute;left:0;width:457px;height:221px}
.split__photo{position:absolute;left:0;top:0;width:236px;height:100%}
.split__panel{position:absolute;left:236px;top:0;width:221px;height:100%;color:var(--white);text-align:center}
.split__kicker{font-weight:300;font-size:17px;line-height:21px}
.split__title{font-weight:700;font-size:17px;line-height:21px}
.split__body{font-size:8.6px;line-height:12.5px;margin-top:14px;padding:0 10px}

.photo-meeting{background:linear-gradient(135deg,#c9b49a 0%,#8a6b4f 45%,#2c3e63 75%,#1d2a47 100%)}
.panel-orange{background:linear-gradient(135deg,var(--orange-hi) 0%,#ef8d10 50%,var(--orange-lo) 100%)}

.finance-dark{top:915px;left:0;width:457px;height:218px;background:linear-gradient(100deg,#0d1c28 0%,#12263a 45%,#27507a 75%,#3f6f9a 100%);color:var(--white)}
.finance-dark__text{position:absolute;left:43px;top:45px}
.finance-dark__kicker{font-weight:300;font-size:20px;line-height:24px}
.finance-dark__title{font-weight:500;font-size:20px;line-height:24px}
.finance-dark__body{font-size:9.6px;line-height:12.5px;margin-top:14px;width:220px}
.finance-dark__body + .finance-dark__body{margin-top:10px}

/* newsletter template */
.header-teal{top:0;left:0;width:457px;height:286px;background:linear-gradient(180deg,#0f2f45 0%,#143f52 50%,#1c5262 100%)}
.header-notch{position:absolute;left:209px;top:285px;width:0;height:0;border-left:20px solid transparent;border-right:20px solid transparent;border-top:17px solid #1c5262}
.services-bg{top:286px;left:0;width:457px;height:301px;background:linear-gradient(180deg,#f8f8f8 0%,#efeff0 55%,#e1e3e5 100%)}
.pin{position:absolute;width:80px;height:92px}
.pin-item__title{position:absolute;width:140px;text-align:center;font-weight:700;font-size:13px;color:var(--ink)}
.pin-item__body{position:absolute;width:120px;text-align:center;font-size:8.6px;line-height:12.3px;color:var(--grey-text)}

.panel-teal{background:linear-gradient(160deg,#1fb0ba 0%,#137482 45%,var(--teal-deep) 100%)}
.field-sunset{top:808px;left:0;width:457px;height:252px;background:linear-gradient(180deg,#e7b36a 0%,#f1c56f 35%,#c9a23e 65%,#8a7a2a 100%)}
.plan-card{position:absolute;left:113px;top:47px;width:243px;height:159px;border:4px solid rgba(255,255,255,.75);border-radius:46px 0 46px 0}
.plan-card__inner{position:absolute;inset:3px;border-radius:40px 0 40px 0;background:#f47b20;color:var(--white);text-align:center;padding-top:17px}
.plan-card__kicker{font-weight:300;font-size:17px;line-height:19px}
.plan-card__title{font-weight:500;font-size:17px;line-height:19px}
.plan-card__body{font-size:8.6px;line-height:12.5px;margin-top:8px}
</style>
</head>
<body>

<svg width="0" height="0" style="position:absolute" aria-hidden="true">
  <defs>
    <symbol id="icon-money" viewBox="0 0 40 40">
      <g fill="none" stroke="currentColor" stroke-width="1.5" stroke-linecap="round" stroke-linejoin="round">
        <path d="M19 8h7l-2 3h-3z"/>
        <circle cx="23" cy="19" r="8"/>
        <path d="M25.5 16c-.5-1-1.5-1.5-2.5-1.5-1.5 0-2.5.8-2.5 2s1 1.6 2.5 2 2.5.9 2.5 2.1-1 2-2.5 2c-1.2 0-2.2-.6-2.6-1.6M23 13v2M23 24v-1.4"/>
        <path d="M5 27h5v8H5zM10 28h5l5 2h6c1.4 0 1.4 2 0 2h-6M26 31l7-3c1.5-.6 2.3 1.2 1 2l-9 5H10"/>
      </g>
    </symbol>
    <symbol id="icon-growth" viewBox="0 0 40 40">
      <g fill="none" stroke="currentColor" stroke-width="1.5" stroke-linecap="round" stroke-linejoin="round">
        <path d="M4 35h32"/>
        <rect x="7" y="27" width="5" height="8"/>
        <rect x="15" y="23" width="5" height="12"/>
        <rect x="23" y="18" width="5" height="17"/>
        <path d="M7 22l8-6 5 3 11-11M26 8h5v5"/>
      </g>
    </symbol>
    <symbol id="icon-secure" viewBox="0 0 40 40">
      <g fill="none" stroke="currentColor" stroke-width="1.5" stroke-linecap="round" stroke-linejoin="round">
        <circle cx="15" cy="8" r="3"/>
        <path d="M9 26v-8c0-3 2.5-5 6-5s6 2 6 5M11 36V26M17 36V27"/>
        <path d="M22 20l7-3 7 3v6c0 5-3 8-7 10-4-2-7-5-7-10z"/>
        <path d="M25.5 26.5l2.5 2.5 4.5-5"/>
      </g>
    </symbol>
    <symbol id="pin-shape" viewBox="0 0 80 92">
      <circle cx="40" cy="39" r="39"/>
      <path d="M27 72L40 88 53 72z"/>
    </symbol>
  </defs>
</svg>

<!-- The Tidegrove Update -->
<section class="template template--update">
  <div class="abs hero-snow" role="img" aria-label="Snow-capped mountain range under soft clouds"></div>

  <div class="brand" style="top:44px;height:60px">
    <span class="brand__dot" style="background:var(--orange)"></span>
    <span class="brand__name" style="color:var(--navy)">Tidegrove</span>
  </div>

  <h1 class="headline" style="top:153px;color:var(--ink)">THE TIDEGROVE<br>UPDATE</h1>
  <div class="date-pill" style="left:160px;top:240px;width:154px;height:40px;background:var(--orange)">MARCH 2020</div>

  <div class="feature-row" style="top:331px">
    <div class="feature-row__badge" style="background:var(--navy);color:var(--white)"><svg width="46" height="46"><use href="#icon-money"/></svg></div>
    <h2 class="feature-row__title" style="top:14px">INVESTMENT</h2>
    <p class="feature-row__body" style="top:35px">Allamcorper est eget tempor cursus neque mi consect etuer mi a ultricies massa est sed nisl aptent</p>
  </div>
  <div class="feature-row" style="top:441px">
    <div class="feature-row__badge" style="background:var(--orange);color:var(--white)"><svg width="46" height="46"><use href="#icon-growth"/></svg></div>
    <h2 class="feature-row__title" style="top:11px">GROWTH</h2>
    <p class="feature-row__body" style="top:32px">Allamcorper est eget tempor cursus neque mi consect etuer mi a ultricies massa est sed nisl aptent</p>
  </div>
  <div class="feature-row" style="top:546px">
    <div class="feature-row__badge" style="background:var(--teal);color:var(--white)"><svg width="46" height="46"><use href="#icon-secure"/></svg></div>
    <h2 class="feature-row__title" style="top:10px">SECURE WEALTH</h2>
    <p class="feature-row__body" style="top:31px">Allamcorper est eget tempor cursus neque mi consect etuer mi a ultricies massa est sed nisl aptent</p>
  </div>

  <div class="split" style="top:661px">
    <div class="split__photo photo-meeting" role="img" aria-label="Advisor and two clients reviewing documents at a table"></div>
    <div class="split__panel panel-orange" style="padding-top:52px">
      <div class="split__kicker">WEALTH</div>
      <div class="split__title">MANAGEMENT</div>
      <p class="split__body" style="margin-top:8px">Pllamcorper est eget tempor cursus neque mi consectetuer mi a ultricies massa<br>Ast sed nisl Class aptent taciti sociosqu ad litora torquent per conubia nostra per inceptos hymenaeos Proin nulla arcu nonummy</p>
    </div>
  </div>

  <div class="abs finance-dark" role="img" aria-label="Glass office towers seen from below">
    <div class="finance-dark__text">
      <div class="finance-dark__kicker">FINANCIAL</div>
      <div class="finance-dark__title">PLANNING SERVICE</div>
      <p class="finance-dark__body">Pllamcorper est eget tempor cursus neque mi consectetuer mi a ultricies massa</p>
      <p class="finance-dark__body">sus eu mattis laoreet viverra sit amet quam Curabitur vel dolor ultrices ipsum dictum tristique Praesent vitae lacus</p>
    </div>
  </div>
</section>

<!-- The Tidegrove Newsletter -->
<section class="template template--newsletter">
  <div class="abs header-teal" role="img" aria-label="Dark teal mountain peaks"></div>
  <div class="header-notch"></div>

  <div class="brand" style="top:26px;height:60px">
    <span class="brand__dot" style="background:var(--white)"></span>
    <span class="brand__name" style="color:var(--white)">Tidegrove</span>
  </div>

  <h1 class="headline" style="top:126px;color:var(--white)">THE TIDEGROVE<br>NEWSLETTER</h1>
  <div class="date-pill" style="left:143px;top:211px;width:171px;height:44px;background:var(--teal)">MARCH 2020</div>

  <div class="abs services-bg" role="img" aria-label="Faint city skyscrapers" style="z-index:0"></div>
  <div class="header-notch" style="z-index:1"></div>

  <svg class="pin" style="left:48px;top:329px;color:var(--teal)"><use href="#pin-shape" fill="currentColor"/></svg>
  <svg class="abs" width="46" height="46" style="left:65px;top:345px;color:var(--white)"><use href="#icon-money"/></svg>
  <h2 class="pin-item__title" style="left:18px;top:426px">INVESTMENT</h2>
  <p class="pin-item__body" style="left:28px;top:449px">Allamcorper est eget tempor cursus neque mi consect etuer mi a ultricies massa est sed nisl aptent</p>

  <svg class="pin" style="left:196px;top:373px;color:var(--night)"><use href="#pin-shape" fill="currentColor"/></svg>
  <svg class="abs" width="46" height="46" style="left:213px;top:389px;color:var(--white)"><use href="#icon-growth"/></svg>
  <h2 class="pin-item__title" style="left:166px;top:470px">GROWTH</h2>
  <p class="pin-item__body" style="left:176px;top:493px">Allamcorper est eget tempor cursus neque mi consect etuer mi a ultricies massa est sed nisl aptent</p>

  <svg class="pin" style="left:343px;top:329px;color:var(--teal)"><use href="#pin-shape" fill="currentColor"/></svg>
  <svg class="abs" width="46" height="46" style="left:360px;top:345px;color:var(--white)"><use href="#icon-secure"/></svg>
  <h2 class="pin-item__title" style="left:313px;top:426px">SECURE WEALTH</h2>
  <p class="pin-item__body" style="left:323px;top:449px">Allamcorper est eget tempor cursus neque mi consect etuer mi a ultricies massa est sed nisl aptent</p>

  <div class="split" style="top:587px">
    <div class="split__photo photo-meeting" role="img" aria-label="Advisor and two clients reviewing documents at a table"></div>
    <div class="split__panel panel-teal" style="padding-top:51px">
      <div class="split__kicker">WEALTH</div>
      <div class="split__title">MANAGEMENT</div>
      <p class="split__body" style="margin-top:8px">Pllamcorper est eget tempor cursus neque mi consectetuer mi a ultricies massa<br>Ast sed nisl Class aptent taciti sociosqu ad litora torquent per conubia nostra per inceptos hymenaeos Proin nulla arcu nonummy</p>
    </div>
  </div>

  <div class="abs field-sunset" role="img" aria-label="Couple walking through a grassy field at sunset">
    <div class="plan-card">
      <div class="plan-card__inner">
        <div class="plan-card__kicker">FINANCIAL</div>
        <div class="plan-card__title">PLANNING SERVICE</div>
        <p class="plan-card__body">Pllamcorper est eget tempor cursus neque mi consectetuer mi a ultricies massa<br>Ast sed nisl Class aptent taciti sociosqu ad litora torquent per conubia nostra per incept</p>
      </div>
    </div>
  </div>
</section>

</body>
</html>
```